Label Design for a New Alcoholized Root Beer

Create a design for a new alcoholized root beer. This is a new product category in the USA growing very rapidly. Root Beer is a popular flavor of Cola, but recently, beer manufacturers have added alcohol to it and have created a new product that has gained traction on the market at a tremendous rate.

Root Beer is vintage product that has been around for a hundred years. Consumers of this product are mostly male between the age of 30 to 45. They purchase this product for its nostalgia and vintage look and taste.

This product will be in a standard 355 mL brown bottle.

It is 5.9% abv.

The name of the product is ''Corvel's Hard Root Beer''.

We have uploaded some pictures of traditional root beers to give you an idea of the feel we want our product to have and also, the bottle the product will be filled in.

Target Market(s)

Consumers are male 30-45, same market as craft beer consumers

Industry/Entity Type

Product

Requirements
Must have
• Design must have a vintage feel to it

```html
<!DOCTYPE html>
<html lang="en">
<head>
<meta charset="utf-8">
<title>Corvel's Hard Root Beer – Label</title>
<link rel="stylesheet" href="https://fonts.googleapis.com/css2?family=Alfa+Slab+One&family=Old+Standard+TT&display=swap">
<style>
  :root {
    --backdrop: #efe9dc;
    --label-cream: #e6d69a;
    --label-navy: #1b2c34;
    --sky-blue: #5db7d2;
    --sky-blue-light: #8fd0e2;
    --horizon-tan: #d9c683;
    --panel-dark: #1d3038;
    --type-light: #f4f1e6;
    --type-gold: #e2cf8c;
  }
  html, body {
    margin: 0;
    padding: 0;
    overflow: hidden;
  }
  body {
    width: 1200px;
    height: 764px;
    background: var(--backdrop);
    display: flex;
    align-items: center;
    justify-content: center;
  }
  .label {
    width: 440px;
    height: 495px;
    display: block;
  }
  .label__border { fill: var(--label-cream); stroke: var(--label-navy); stroke-width: 5; }
  .label__inner-rule { fill: none; stroke: var(--label-navy); stroke-width: 3; }
  .label__horizon { fill: var(--horizon-tan); }
  .label__panel { fill: var(--panel-dark); }
  .label__stitch { fill: none; stroke: var(--type-light); stroke-width: 1.2; stroke-dasharray: 3 3; opacity: .85; }
  .label__brand {
    font-family: "Alfa Slab One", serif;
    font-size: 50px;
    fill: var(--label-navy);
  }
  .label__product {
    font-family: "Alfa Slab One", serif;
    font-size: 27px;
    letter-spacing: 1px;
    fill: var(--type-light);
  }
  .label__abv {
    font-family: "Old Standard TT", serif;
    font-size: 17px;
    fill: var(--type-gold);
  }
</style>
</head>
<body>
  <svg class="label" viewBox="0 0 360 405" xmlns="http://www.w3.org/2000/svg" aria-label="Corvel's Hard Root Beer bottle label">
    <defs>
      <clipPath id="label-field">
        <path d="M24 378 L24 162 C24 72 98 20 180 20 C262 20 336 72 336 162 L336 378 Q180 346 24 378 Z"/>
      </clipPath>
      <linearGradient id="sky-fill" x1="0" y1="0" x2="0" y2="1">
        <stop offset="0" stop-color="var(--sky-blue)"/>
        <stop offset="1" stop-color="var(--sky-blue-light)"/>
      </linearGradient>
    </defs>

    <path class="label__border" d="M8 398 L8 160 C8 58 88 4 180 4 C272 4 352 58 352 160 L352 398 Q180 360 8 398 Z"/>

    <g clip-path="url(#label-field)">
      <rect class="label__sky" x="0" y="0" width="360" height="200" fill="url(#sky-fill)" role="img" aria-label="Sunburst rays rising over the horizon"/>
      <path class="label__horizon" d="M0 188 Q180 142 360 188 L360 405 L0 405 Z"/>
      <path class="label__panel" d="M0 262 C70 236 120 252 180 246 C240 240 300 238 360 222 L360 405 L0 405 Z"/>
      <path class="label__stitch" d="M30 268 C90 248 130 260 180 255 C240 249 290 248 330 236"/>
      <path class="label__stitch" d="M32 366 Q180 336 328 366"/>
    </g>

    <path class="label__inner-rule" d="M24 378 L24 162 C24 72 98 20 180 20 C262 20 336 72 336 162 L336 378 Q180 346 24 378 Z"/>

    <text class="label__brand" x="180" y="214" text-anchor="middle">Corvel's</text>
    <text class="label__product" x="180" y="290" text-anchor="middle">HARD ROOT</text>
    <text class="label__product" x="180" y="318" text-anchor="middle">BEER</text>
    <text class="label__abv" x="180" y="340" text-anchor="middle">5.9% abv.</text>
  </svg>
</body>
</html>
```